Modifications to a letterhead design

The following changes are being made to show other options for staff. Thanks

Part A - Letterhead
I have the two letterheads that I need a slight change made. I have already turned them into templates. So I hope the changes to the design can still occur.
Where the school name is, could you remove the yellow line and brown shape. Instead, please write:

Brell Tanner Ridge High School

The colour is to be in the chocolate brown colour. The font size and positioning for the school name can stay the same.

Changes to occur for colour and black&white

Part B - Certificates

Principal Award:
- Where the school name is, could you remove the yellow line and brown shape. Instead, please write: Brell Tanner Ridge High School
The colour is to be in the chocolate brown colour. The font size remains the same and it needs to be centred on the page
- Please remove the purple box and have no box
- for the 5 award categories please have not dot before the word, and centre the 5 categories and ensure the first letter is in capitals but the rest of the letters are lower case, for example: School Service
- Please remove the principal banner and change to ribbon on page 2 of the slide show - you will need to tidy it up or create new as I just cut and pasted it
- then could I have 2 Principal Awards - one addressing the above, and a second one addressing those things mentioned above plus removing all the colour at the bottom of the page

Year Advisor Award
- Use the same template design for the Principal Award mentioned above (including the details mentioned above). This time change the name on the ribbon (on page 2 of powerpoint) to Year Adviser's Award (only fist letter is capital , the rest lower case).
- Also, for the Year Adviser's Award, please produce 5 certificates with 1 category on each certificate e.g. School Service (again only first letter in capitals, the rest lower case). Also, the 5 certificates have a changed colour at the bottom of the page (including the 3 twirling ribbons). Colours for the bottom of the certificates are: Green, purple, red, yellow and blue.
- Please also create the 5 Year Adviser certificates without any colour at the bottom as well

```html
<!DOCTYPE html>
<html lang="en">
<head>
<meta charset="utf-8">
<title>Brell Tanner Ridge High School – Letterhead options</title>
<link rel="stylesheet" href="https://fonts.googleapis.com/css2?family=Vollkorn:ital,wght@0,400;1,700&family=Arimo:wght@400&display=swap">
<style>
  :root {
    --page-bg: #ece8df;
    --card-bg: #ffffff;
    --mono-band: #8c8c8c;
    --mono-band-light: #c4c4c4;
    --mono-text: #8a8a8a;
    --mono-icon: #7a7a7a;
    --purple: #9c4197;
    --yellow: #f6e500;
    --chocolate: #3d1616;
    --chocolate-name: #4a2424;
    --ink: #1f1f1f;
  }
  * { box-sizing: border-box; margin: 0; padding: 0; }
  html, body {
    width: 1200px; height: 765px; overflow: hidden;
    background: var(--page-bg);
  }
  .canvas { position: relative; width: 1200px; height: 765px; }

  .letterhead {
    position: absolute; left: 90px; width: 1020px;
    background: var(--card-bg);
    box-shadow: 0 2px 6px rgba(0,0,0,.18);
    overflow: hidden;
  }
  .letterhead--mono { top: 110px; height: 266px; --tone: var(--mono-text); --icon: var(--mono-icon); --name: var(--mono-text); }
  .letterhead--colour { top: 425px; height: 222px; --tone: var(--ink); --icon: var(--purple); --name: var(--chocolate-name); }

  .header-band { position: absolute; left: 0; top: 0; width: 1020px; }

  .crest-mark {
    position: absolute; width: 125px;
    display: flex; flex-direction: column; align-items: center; gap: 8px;
  }
  .crest-mark__dot { width: 52px; height: 52px; border-radius: 50%; background: var(--icon); }
  .crest-mark__name {
    font-family: "Vollkorn", serif; font-size: 14px; line-height: 1.15;
    color: var(--name); text-align: center;
  }

  .school-name {
    position: absolute; left: 197px;
    font-family: "Vollkorn", serif; font-weight: 400; font-size: 24.5px;
    color: var(--name); white-space: nowrap; line-height: 1;
  }
  .principal {
    position: absolute; left: 197px;
    font-family: "Arimo", Arial, sans-serif; font-size: 12.6px; line-height: 17px;
    color: var(--tone); white-space: nowrap;
  }
  .motto {
    position: absolute; left: 197px;
    font-family: "Vollkorn", serif; font-style: italic; font-weight: 700; font-size: 15px;
    color: var(--tone); white-space: nowrap;
  }
  .letterhead--colour .motto { color: var(--chocolate); }

  .contacts { position: absolute; list-style: none; }
  .contacts li {
    display: flex; align-items: center; gap: 8px; height: 22px;
    font-family: "Arimo", Arial, sans-serif; font-size: 12.8px; color: var(--tone);
    white-space: nowrap;
  }
  .contact-icon { width: 15px; height: 15px; flex: none; }
  .contact-icon circle { fill: var(--icon); }
  .contact-icon .glyph { fill: none; stroke: #fff; stroke-width: 1.3; stroke-linejoin: round; }
  .contact-icon .glyph-fill { fill: #fff; }
</style>
</head>
<body>
<main class="canvas">

  <section class="letterhead letterhead--mono" aria-label="Black and white letterhead">
    <svg class="header-band" viewBox="0 0 1020 110" width="1020" height="110" aria-hidden="true">
      <path fill="var(--mono-band-light)" d="M0,0 L1020,0 L1020,28 Q520,58 0,34 Z"/>
      <path fill="var(--mono-band)" d="M0,42 Q520,68 1020,36 L1020,62 Q520,96 0,70 Z"/>
      <path fill="none" stroke="var(--mono-band)" stroke-width="2" d="M0,84 Q520,112 1020,76"/>
    </svg>

    <div class="crest-mark" style="left:44px; top:118px;">
      <span class="crest-mark__dot"></span>
      <span class="crest-mark__name">Brell Tanner Ridge</span>
    </div>

    <h1 class="school-name" style="top:128px;">Brell Tanner Ridge High School</h1>
    <p class="principal" style="top:170px;">Principal: Mr Dorian Pellow BA, DipEd,<br>GCertLead, MEd(Curric), NSW JP</p>
    <p class="motto" style="top:213px;">“Steady hands, open minds, true hearts”</p>

    <ul class="contacts" style="left:676px; top:95px;">
      <li><svg class="contact-icon" viewBox="0 0 16 16"><circle cx="8" cy="8" r="8"/><path class="glyph-fill" d="M5,4 L7,4 L7.6,6.3 L6.6,7 C7,8 8,9 9,9.4 L9.7,8.4 L12,9 L12,11 C8,11.5 4.5,8 5,4 Z"/></svg>02 5550 3172</li>
      <li><svg class="contact-icon" viewBox="0 0 16 16"><circle cx="8" cy="8" r="8"/><rect class="glyph" x="4" y="6.5" width="8" height="4"/><rect class="glyph" x="5.5" y="4" width="5" height="2.5"/><rect class="glyph" x="5.5" y="9.5" width="5" height="2.5"/></svg>02 5550 3189</li>
      <li><svg class="contact-icon" viewBox="0 0 16 16"><circle cx="8" cy="8" r="8"/><rect class="glyph" x="4" y="5" width="8" height="6"/><path class="glyph" d="M4,5 L8,8.5 L12,5"/></svg>office@brelltanner.example.edu</li>
      <li><svg class="contact-icon" viewBox="0 0 16 16"><circle cx="8" cy="8" r="8"/></svg>http://btrhs.portal.example.com</li>
      <li><svg class="contact-icon" viewBox="0 0 16 16"><circle cx="8" cy="8" r="8"/></svg>https://social.example.com/brelltannerridge</li>
      <li><svg class="contact-icon" viewBox="0 0 16 16"><circle cx="8" cy="8" r="8"/><rect class="glyph" x="4" y="4.5" width="8" height="5.5"/><path class="glyph" d="M8,10 L8,12 M6,12 L10,12"/></svg>https://brelltanner.schools.example.edu</li>
      <li><svg class="contact-icon" viewBox="0 0 16 16"><circle cx="8" cy="8" r="8"/></svg>https://video.example.com/user40215583</li>
    </ul>
  </section>

  <section class="letterhead letterhead--colour" aria-label="Colour letterhead">
    <svg class="header-band" viewBox="0 0 1020 70" width="1020" height="70" aria-hidden="true">
      <path fill="var(--purple)" d="M0,0 L1020,0 L1020,26 Q520,50 0,28 Z"/>
      <path fill="var(--yellow)" d="M0,34 Q520,56 1020,32 L1020,40 Q520,64 0,42 Z"/>
      <path fill="none" stroke="var(--chocolate)" stroke-width="2" d="M0,50 Q520,74 1020,46"/>
    </svg>

    <div class="crest-mark" style="left:44px; top:80px;">
      <span class="crest-mark__dot"></span>
      <span class="crest-mark__name">Brell Tanner Ridge</span>
    </div>

    <h1 class="school-name" style="top:94px;">Brell Tanner Ridge High School</h1>
    <p class="principal" style="top:133px;">Principal: Mr Dorian Pellow BA, DipEd,<br>GCertLead, MEd(Curric), NSW JP</p>
    <p class="motto" style="top:176px;">“Steady hands, open minds, true hearts”</p>

    <ul class="contacts" style="left:674px; top:58px;">
      <li><svg class="contact-icon" viewBox="0 0 16 16"><circle cx="8" cy="8" r="8"/><path class="glyph-fill" d="M5,4 L7,4 L7.6,6.3 L6.6,7 C7,8 8,9 9,9.4 L9.7,8.4 L12,9 L12,11 C8,11.5 4.5,8 5,4 Z"/></svg>02 5550 3172</li>
      <li><svg class="contact-icon" viewBox="0 0 16 16"><circle cx="8" cy="8" r="8"/><rect class="glyph" x="4" y="6.5" width="8" height="4"/><rect class="glyph" x="5.5" y="4" width="5" height="2.5"/><rect class="glyph" x="5.5" y="9.5" width="5" height="2.5"/></svg>02 5550 3189</li>
      <li><svg class="contact-icon" viewBox="0 0 16 16"><circle cx="8" cy="8" r="8"/><rect class="glyph" x="4" y="5" width="8" height="6"/><path class="glyph" d="M4,5 L8,8.5 L12,5"/></svg>office@brelltanner.example.edu</li>
      <li><svg class="contact-icon" viewBox="0 0 16 16"><circle cx="8" cy="8" r="8"/></svg>http://btrhs.portal.example.com</li>
      <li><svg class="contact-icon" viewBox="0 0 16 16"><circle cx="8" cy="8" r="8"/></svg>https://social.example.com/brelltannerridge</li>
      <li><svg class="contact-icon" viewBox="0 0 16 16"><circle cx="8" cy="8" r="8"/><rect class="glyph" x="4" y="4.5" width="8" height="5.5"/><path class="glyph" d="M8,10 L8,12 M6,12 L10,12"/></svg>https://brelltanner.schools.example.edu</li>
      <li><svg class="contact-icon" viewBox="0 0 16 16"><circle cx="8" cy="8" r="8"/></svg>https://video.example.com/user40215583</li>
    </ul>
  </section>

</main>
</body>
</html>
```